Essential Capacities Mouse Mat

Seeking to design a mouse mat for distribution to employees that captures the Essential Capacities (see attached file).
The design should embody the 7 categories, be visual, ideally be icon based.

Mouse mat size:
9.25" x 7.68"
235 x 195 mm
2776 x 2303 pixels

Fonts:
Linden Harbor Academy (Arial)
LINDEN HARBOR ACADEMY (Agency FB, bold/all capitals)

Font styles to use
Sans Serif

Colors
0455a3
ffc214
6b449b
ec1f27
f37122
9bcb3b

Requirements
Must have
• The 7 Essential Capacities Headings must be incorporated in the design.

```html
<!DOCTYPE html>
<html lang="en">
<head>
<meta charset="utf-8">
<title>Essential Capacities Mouse Mat</title>
<link href="https://fonts.googleapis.com/css2?family=Roboto+Condensed:wght@400;500&display=swap" rel="stylesheet">
<style>
  :root {
    --blue: #0455a3;
    --yellow: #ffc214;
    --purple: #6b449b;
    --red: #ec1f27;
    --orange: #f37122;
    --green: #9bcb3b;
    --pink: #ff55b8;
    --ink: #111111;
    --paper: #ffffff;
  }
  html, body {
    margin: 0;
    padding: 0;
    width: 1200px;
    height: 1031px;
    overflow: hidden;
    background: var(--paper);
  }
  .mat {
    position: relative;
    width: 1200px;
    height: 1031px;
    font-family: "Roboto Condensed", "Arial Narrow", sans-serif;
  }
  .tile {
    position: absolute;
    width: 375px;
    height: 320px;
    border-radius: 24px;
    display: flex;
    align-items: center;
    justify-content: center;
    text-align: center;
    box-sizing: border-box;
    color: var(--paper);
    font-weight: 500;
    font-size: 37px;
    line-height: 52px;
    text-transform: uppercase;
    letter-spacing: -0.3px;
  }
  .col-1 { left: 13px; }
  .col-2 { left: 410px; }
  .col-3 { left: 806px; }
  .row-1 { top: 18px; }
  .row-2 { top: 354px; }
  .row-3 { top: 690px; }

  .tile--title {
    background: var(--paper);
    border: 8px solid var(--ink);
    border-radius: 34px;
    color: var(--ink);
    text-transform: none;
    font-weight: 400;
    font-size: 32px;
    line-height: 46px;
    letter-spacing: -0.2px;
  }
  .tile--analytical { background: var(--blue); }
  .tile--communication { background: var(--yellow); }
  .tile--leadership { background: var(--purple); }
  .tile--digital { background: var(--red); }
  .tile--global { background: var(--orange); }
  .tile--adaptability { background: #9fc94a; }
  .tile--integrity { background: var(--pink); }

  .school-name {
    position: absolute;
    left: 806px;
    top: 690px;
    width: 375px;
    height: 320px;
    display: flex;
    flex-direction: column;
    align-items: center;
    justify-content: center;
    gap: 16px;
    color: var(--ink);
    font-weight: 500;
    font-size: 26px;
    letter-spacing: 0.5px;
    text-align: center;
  }
  .school-name__dot {
    width: 70px;
    height: 70px;
    border-radius: 50%;
    background: var(--ink);
  }
</style>
</head>
<body>
<main class="mat">
  <div class="tile tile--title col-1 row-1">Essential Capacities for<br>the 21st Century Schools<br>of the Future Committee<br>CIEA Commission on<br>Accreditation</div>
  <div class="tile tile--analytical col-2 row-1">Analytical<br>&amp; Creative Thinking<br>and<br>Problem-Solving</div>
  <div class="tile tile--communication col-3 row-1">Complex<br>Communication<br>– Oral and Written</div>
  <div class="tile tile--leadership col-1 row-2">Leadership<br>and<br>Teamwork</div>
  <div class="tile tile--digital col-2 row-2">Digital<br>and<br>Quantitative<br>Literacy</div>
  <div class="tile tile--global col-3 row-2">Global Perspective</div>
  <div class="tile tile--adaptability col-1 row-3">Adaptability,<br>Initiative, and<br>Risk-Taking</div>
  <div class="tile tile--integrity col-2 row-3">Integrity<br>and<br>Ethical<br>Decision-Making</div>
  <div class="school-name">
    <span class="school-name__dot"></span>
    <span>LINDEN HARBOR ACADEMY</span>
  </div>
</main>
</body>
</html>
```